Christmas Flyer

Hi,
We are needing a flyer that communicates a Christmas message for our cafe.
We'd like to advertise:
"To all of our loyal customers, if you are lucky enough to be working Christmas Day, we will be open and serving you FREE COFFEE from 6am - 10am.
Thank you for all your support over the last 12 months, we hope you have a very Merry Christmas, and have a happy and safe holidays from Tinker Lane Kitchen"

I have included our logo, and one of our previous flyers.

You can also check out our instagram. Instagram @tinkerlanekitchen

Industry/Entity Type

Cafe

```html
<!DOCTYPE html>
<html lang="en">
<head>
<meta charset="utf-8">
<title>Tinker Lane Kitchen – Christmas Flyer</title>
<link rel="stylesheet" href="https://fonts.googleapis.com/css2?family=Cinzel:wght@700&family=Didact+Gothic&display=swap">
<style>
  :root {
    --red-deep: #b30f12;
    --red-mid: #e0191c;
    --red-glow: #ff5a4a;
    --tree-green: #1f9a3a;
    --tree-dark: #137a2a;
    --star-gold: #c9b23a;
    --ink-white: #ffffff;
    --logo-red: #d8182a;
    --logo-bg: #ffffff;
  }
  * { margin: 0; padding: 0; box-sizing: border-box; }
  html, body {
    width: 849px;
    height: 1200px;
    overflow: hidden;
    background: var(--red-deep);
  }
  .flyer {
    position: relative;
    width: 849px;
    height: 1200px;
    overflow: hidden;
    color: var(--ink-white);
    text-align: center;
  }
  .flyer__backdrop {
    position: absolute;
    inset: 0;
    background:
      radial-gradient(ellipse 55% 45% at 50% 48%, var(--red-glow) 0%, rgba(255,90,74,0) 70%),
      radial-gradient(ellipse 90% 80% at 50% 45%, var(--red-mid) 0%, var(--red-deep) 100%);
  }
  .flyer__tree {
    position: absolute;
    left: 300px;
    top: 37px;
    width: 267px;
    height: 296px;
    background: linear-gradient(180deg, var(--star-gold) 0%, var(--tree-green) 18%, var(--tree-dark) 100%);
    border-radius: 6px;
  }
  .message__line {
    position: absolute;
    left: 0;
    width: 100%;
    top: var(--y);
    transform: translateY(-50%);
    white-space: nowrap;
    text-shadow: 0 0 6px rgba(255,255,255,0.35);
  }
  .message__line--light {
    font-family: "Didact Gothic", sans-serif;
    font-size: 37px;
    letter-spacing: 0.5px;
  }
  .message__line--bold {
    font-family: "Cinzel", serif;
    font-weight: 700;
    font-size: 39px;
  }
  .message__line--big {
    font-size: 48px;
  }
  .message__line--signoff {
    font-size: 30px;
  }
  .message__brand {
    font-family: "Cinzel", serif;
    font-weight: 700;
    font-size: 34px;
  }
  .brand-mark {
    position: absolute;
    left: 320px;
    top: 993px;
    width: 200px;
    height: 147px;
    background: var(--logo-bg);
    display: flex;
    flex-direction: column;
    align-items: center;
    justify-content: center;
    gap: 8px;
  }
  .brand-mark__dot {
    width: 22px;
    height: 22px;
    border-radius: 50%;
    background: var(--logo-red);
  }
  .brand-mark__name {
    font-family: "Cinzel", serif;
    font-weight: 700;
    font-size: 22px;
    line-height: 1.1;
    color: var(--logo-red);
    white-space: normal;
    width: 170px;
  }
</style>
</head>
<body>
  <main class="flyer">
    <div class="flyer__backdrop" role="img" aria-label="Red background with radiating light rays and white sparkles"></div>
    <div class="flyer__tree" role="img" aria-label="Green Christmas tree with a gold star on top"></div>

    <section class="message">
      <p class="message__line message__line--light" style="--y:364px">TO ALL OF OUR LOYAL CUSTOMERS,</p>
      <p class="message__line message__line--light" style="--y:407px">IF YOU ARE LUCKY ENOUGH TO BE</p>
      <p class="message__line message__line--light" style="--y:449px">WORKING CHRISTMAS DAY,</p>
      <p class="message__line message__line--bold" style="--y:524px">We Will Be Open and Serving You</p>
      <p class="message__line message__line--bold message__line--big" style="--y:573px">Free Coffee from 6-10am.</p>
      <p class="message__line message__line--light" style="--y:627px">THANK YOU FOR ALL YOUR SUPPORT</p>
      <p class="message__line message__line--light" style="--y:677px">OVER THE LAST 12 MONTHS,</p>
      <p class="message__line message__line--bold" style="--y:731px">We Hope You Have a</p>
      <p class="message__line message__line--bold" style="--y:780px">Very Merry Christmas!</p>
      <p class="message__line message__line--light" style="--y:837px">AND HAVE A HAPPY</p>
      <p class="message__line message__line--light" style="--y:887px">AND SAFE HOLIDAYS</p>
      <p class="message__line message__line--light message__line--signoff" style="--y:944px">FROM <span class="message__brand">Tinker Lane Kitchen</span>!</p>
    </section>

    <div class="brand-mark">
      <span class="brand-mark__dot"></span>
      <span class="brand-mark__name">Tinker Lane Kitchen</span>
    </div>
  </main>
</body>
</html>
```